One of a Kind Clean Business Card

We need to design a new business card template for our company. Our company designs and produced merchandising displays. You can see a sample of what we produce on our site www.qorvatfixtures.com. I have uploaded our logo in vector format, as well as a picture of our current business cards. We want a totally different look. We want simple and clean, looking forward to seeing what people create.
Updates

I would like to update the address for Tellur Display Group Inc. 418 N Brindle Ave Arlington Heights, IL 60817 Would also note. No QR codes

Industry/Entity Type

Business

Contact Information for Business Card

Need a 1 sided business card designed.

Font styles to use
Serif

Requirements
Must have
• Easy to view; Clean Design
Nice to have
• Features that promote engineering and creativity
Should not have
• Too much clutter, keep it simple

```html
<!DOCTYPE html>
<html lang="en">
<head>
<meta charset="utf-8">
<title>Tellur Display Group Inc. – Business Card</title>
<link href="https://fonts.googleapis.com/css2?family=Lato:wght@400;700&family=Open+Sans:wght@400;600&display=swap" rel="stylesheet">
<style>
  :root {
    --page-bg: #e4e6e8;
    --card-bg: #f7f8f8;
    --panel-dark: #1b1c1f;
    --accent-red: #8c1c24;
    --text-light: #ffffff;
    --text-name: #e9e9ea;
    --text-dark: #1e1e20;
  }
  html, body {
    margin: 0;
    width: 1200px;
    height: 900px;
    overflow: hidden;
    background: var(--page-bg);
  }
  .business-card {
    position: absolute;
    left: 100px;
    top: 166px;
    width: 1000px;
    height: 568px;
    background: var(--card-bg);
    box-shadow: 0 10px 30px rgba(0,0,0,0.18);
    overflow: hidden;
  }
  .card-shapes {
    position: absolute;
    inset: 0;
    width: 100%;
    height: 100%;
  }
  .contact-block {
    position: absolute;
    right: 76px;
    top: 62px;
    text-align: right;
    font-family: "Lato", sans-serif;
    color: var(--text-light);
  }
  .person-name {
    margin: 0 0 26px;
    font-size: 50px;
    font-weight: 700;
    color: var(--text-name);
    line-height: 1;
  }
  .person-name .surname { color: var(--accent-red); }
  .contact-line {
    margin: 0;
    font-size: 27px;
    line-height: 37px;
  }
  .contact-line.gap-before { margin-top: 6px; }
  .company-name {
    position: absolute;
    left: 80px;
    top: 420px;
    margin: 0;
    font-family: "Open Sans", sans-serif;
    font-weight: 400;
    font-size: 40px;
    color: var(--accent-red);
    line-height: 1;
  }
  .company-address {
    position: absolute;
    left: 80px;
    top: 494px;
    margin: 0;
    font-family: "Open Sans", sans-serif;
    font-size: 21px;
    color: var(--text-dark);
  }
</style>
</head>
<body>
  <main class="business-card">
    <svg class="card-shapes" viewBox="0 0 748 425" preserveAspectRatio="none" aria-hidden="true">
      <polygon class="accent-stripe" points="162,0 196,0 560,425 556,425" fill="var(--accent-red)"/>
      <polygon class="dark-panel" points="192,0 748,0 748,425 560,425" fill="var(--panel-dark)"/>
    </svg>

    <section class="contact-block">
      <h1 class="person-name">Dale <span class="surname">Morrow</span></h1>
      <p class="contact-line">815-555-0147</p>
      <p class="contact-line">312-555-0193</p>
      <p class="contact-line gap-before">dmorrow@qorvatfixtures.com</p>
      <p class="contact-line">www.qorvatfixtures.com</p>
    </section>

    <h2 class="company-name">Tellur Display Group Inc.</h2>
    <p class="company-address">418 N Brindle Ave Arlington Heights, IL 60817</p>
  </main>
</body>
</html>
```